Word document template for sales proposals

I am after a template that is simple but impactful. Use of colour to be limited but some for impact would be good. The proposals are for use in the professional technical field.

```html
<!DOCTYPE html>
<html lang="en">
<head>
<meta charset="utf-8">
<title>Sales Proposal Template</title>
<link href="https://fonts.googleapis.com/css2?family=Montserrat:ital,wght@0,300;0,400;0,600;0,700;0,800;0,900;1,400&family=Open+Sans:wght@400&display=swap" rel="stylesheet">
<style>
:root{
  --orange:#f28c28;
  --orange-dark:#c8661a;
  --blue:#29a8e0;
  --ink:#1e1e1e;
  --text:#2b2b2b;
  --canvas:#e0e0e0;
  --white:#ffffff;
}
*{box-sizing:border-box;margin:0;padding:0}
html,body{width:1200px;height:1200px;overflow:hidden;background:var(--canvas)}
body{position:relative;font-family:"Open Sans",sans-serif;color:var(--text)}
.page{position:absolute;width:577px;height:815px;background:var(--white);overflow:hidden;transform:scale(.6211);transform-origin:0 0;box-shadow:0 3px 10px rgba(0,0,0,.25)}
.page-cover{left:39px;top:93px}
.page-about{left:420px;top:93px}
.page-coop{left:802px;top:93px}
.page-team{left:225px;top:637px}
.page-end{left:616px;top:637px}
.shape{position:absolute;inset:0}
.photo{position:absolute}
.photo-building{background:linear-gradient(160deg,#6d5a44 0%,#9fb7c2 35%,#2f5560 70%,#1c2e33 100%)}
.photo-desk{background:linear-gradient(120deg,#3b2f25,#7c6450 45%,#d8d4cc 80%,#5a4634)}
.photo-group{background:linear-gradient(120deg,#9a8a78,#c9a48e 45%,#8a6c5c 75%,#5b4a44)}
.brand{position:absolute;display:flex;align-items:center;gap:7px;font-family:"Montserrat",sans-serif;font-weight:700;font-size:17px;letter-spacing:.5px;color:var(--orange)}
.brand-dot{width:14px;height:14px;border-radius:50%;background:var(--blue)}
.brand-light{color:var(--white)}
.brand-light .brand-dot{background:var(--white)}
.page-no{position:absolute;right:30px;top:42px;font-family:"Montserrat",sans-serif;font-weight:700;font-size:27px;color:var(--white)}
.footer{position:absolute;left:0;right:0;bottom:0;height:77px;background:var(--ink);font-family:"Montserrat",sans-serif;font-size:12.5px;color:var(--white)}
.footer-blue{background:var(--blue)}
.contact{position:absolute;display:flex;align-items:center;gap:14px}
.contact svg{width:15px;height:15px;fill:var(--white)}
.footer-blue .contact svg{fill:var(--orange)}
.c1{left:44px;top:16px}.c2{left:44px;top:42px}.c3{left:328px;top:17px}.c4{left:328px;top:43px}
.body-copy{font-size:12px;line-height:1.35;text-align:justify;color:var(--text)}
.h-display{font-family:"Montserrat",sans-serif;font-weight:800}

/* cover */
.cover-kicker{position:absolute;left:58px;top:493px;font-family:"Montserrat",sans-serif;font-weight:300;font-size:28px;color:var(--blue);display:flex;align-items:center;gap:40px}
.cover-kicker::after{content:"";width:80px;height:1.5px;background:var(--orange)}
.cover-title{position:absolute;left:58px;top:528px;font-size:49px;color:var(--orange)}
.rule{position:absolute;height:4px;width:62px;background:var(--orange)}
.cover-lead{position:absolute;left:58px;top:636px;width:400px;font-family:"Montserrat",sans-serif;font-weight:300;font-size:12.5px;line-height:1.65;color:var(--blue)}

/* about */
.about-title{position:absolute;left:68px;top:376px;font-size:35px;line-height:1.1;color:var(--white)}
.about-col{position:absolute;top:500px;width:215px}
.about-col-a{left:60px;font-size:12px;line-height:1.35}
.about-col-b{left:305px;font-size:11px}

/* cooperation */
.coop-title{position:absolute;left:58px;top:125px;font-size:29px;line-height:1.13;color:var(--white)}
.coop-copy{position:absolute;left:58px;width:462px;font-size:10.8px}
.team-point{position:absolute;top:590px;width:208px}
.team-point h3{display:flex;align-items:center;gap:14px;font-family:"Montserrat",sans-serif;font-weight:700;font-size:22px;color:var(--ink);margin-bottom:6px}
.team-point h3::before{content:"";width:21px;height:21px;border-radius:50%;background:var(--orange)}
.team-point p{font-size:10.8px;line-height:1.35;text-align:justify}

/* team */
.team-title{position:absolute;left:0;right:0;top:142px;text-align:center;font-size:30px;color:var(--orange)}
.member{position:absolute;width:143px;text-align:center;font-family:"Montserrat",sans-serif}
.member .portrait{height:148px;background:linear-gradient(160deg,#b9a89a,#7d6a5e 60%,#4a3f3a)}
.member h4{margin-top:12px;font-weight:700;font-size:12.5px;color:var(--ink)}
.member p{margin-top:5px;font-style:italic;font-size:12px;color:var(--text)}

/* end */
.end-kicker{position:absolute;left:58px;top:503px;font-family:"Montserrat",sans-serif;font-size:16px;color:var(--ink);display:flex;align-items:center;gap:12px}
.end-kicker::after{content:"";width:57px;height:1.5px;background:var(--orange)}
.end-title{position:absolute;left:58px;top:528px;font-weight:900;font-size:52px;line-height:.96;color:#0d0d0d}
.end-lead{position:absolute;left:58px;top:658px;width:400px;font-family:"Montserrat",sans-serif;font-size:12.5px;line-height:1.4;color:var(--text)}
</style>
</head>
<body>
<svg width="0" height="0" style="position:absolute" aria-hidden="true">
  <symbol id="i-globe" viewBox="0 0 16 16"><path d="M8 1a7 7 0 1 0 0 14A7 7 0 0 0 8 1zm0 1.3c.7.6 1.3 1.8 1.6 3.2H6.4C6.7 4.1 7.3 2.9 8 2.3zM5.1 5.5H2.9a5.7 5.7 0 0 1 3-2.7 8 8 0 0 0-.8 2.7zm-2.6 1.3h2.5a12 12 0 0 0 0 2.4H2.5a5.7 5.7 0 0 1 0-2.4zm.4 3.7h2.2c.2 1 .4 1.9.8 2.7a5.7 5.7 0 0 1-3-2.7zM8 13.7c-.7-.6-1.3-1.8-1.6-3.2h3.2c-.3 1.4-.9 2.6-1.6 3.2zm-1.8-4.5a11 11 0 0 1 0-2.4h3.6a11 11 0 0 1 0 2.4zm3.9 3.9c.4-.8.6-1.7.8-2.6h2.2a5.7 5.7 0 0 1-3 2.6zm1-3.9a12 12 0 0 0 0-2.4h2.5a5.7 5.7 0 0 1 0 2.4zm.9-3.7h-2.2a8 8 0 0 0-.8-2.7 5.7 5.7 0 0 1 3 2.7z"/></symbol>
  <symbol id="i-pin" viewBox="0 0 16 16"><path d="M8 0a5.5 5.5 0 0 0-5.5 5.5C2.5 10 8 16 8 16s5.5-6 5.5-10.5A5.5 5.5 0 0 0 8 0zm0 7.8a2.3 2.3 0 1 1 0-4.6 2.3 2.3 0 0 1 0 4.6z"/></symbol>
  <symbol id="i-phone" viewBox="0 0 16 16"><path d="M3.6 1l2.3 2.8-1.3 1.7a9 9 0 0 0 5.9 5.9l1.7-1.3L15 12.4l-1.6 2.3C7.3 15.3.7 8.7 1.3 2.6z"/></symbol>
  <symbol id="i-mail" viewBox="0 0 16 16"><path d="M1 3h14v1.2L8 8.6 1 4.2zm0 2.6l7 4.4 7-4.4V13H1z"/></symbol>
</svg>

<!-- Cover -->
<section class="page page-cover">
  <div class="brand" style="left:30px;top:55px"><span class="brand-dot"></span>CORVANE</div>
  <svg class="shape" viewBox="0 0 577 815" aria-hidden="true">
    <polygon points="0,108 112,108 258,478 0,478" fill="var(--orange)"/>
    <polygon points="375,120 425,33 445,120" fill="var(--blue)"/>
    <polygon points="425,33 490,33 577,190 577,265" fill="#f7941d"/>
    <polygon points="236,442 272,442 252,478" fill="var(--blue)"/>
  </svg>
  <div class="photo photo-building" role="img" aria-label="Upward view of a glass office tower framed by tree branches" style="left:0;top:122px;width:577px;height:320px;clip-path:polygon(112px 0,577px 0,577px 320px,236px 320px)"></div>
  <div class="cover-kicker">Business</div>
  <h1 class="cover-title h-display">Proposal</h1>
  <div class="rule" style="left:58px;top:615px"></div>
  <p class="cover-lead">A proposal sets out the scope, method and cost of the work we offer. It is prepared for each client and explains clearly what will be delivered, when and how.</p>
  <footer class="footer footer-blue">
    <div class="contact c1"><svg><use href="#i-globe"/></svg>www.corvanetech.com</div>
    <div class="contact c2"><svg><use href="#i-pin"/></svg>48 Harbor Row, Westfield</div>
    <div class="contact c3"><svg><use href="#i-phone"/></svg>+1-555-014-2290</div>
    <div class="contact c4"><svg><use href="#i-mail"/></svg>hello@corvanetech.com</div>
  </footer>
</section>

<!-- About -->
<section class="page page-about">
  <div class="photo photo-desk" role="img" aria-label="Team members bumping fists over a desk with laptops, papers and phones" style="left:0;top:138px;width:577px;height:319px"></div>
  <svg class="shape" viewBox="0 0 577 815" aria-hidden="true">
    <polygon points="270,22 577,22 577,98 300,98" fill="var(--ink)"/>
    <polygon points="0,18 270,18 300,108 0,108" fill="var(--orange)"/>
    <polygon points="337,0 352,0 402,72 387,72" fill="var(--orange)"/>
    <polygon points="0,358 275,358 318,468 0,468" fill="var(--orange)"/>
  </svg>
  <div class="brand brand-light" style="left:65px;top:52px"><span class="brand-dot"></span>CORVANE</div>
  <div class="page-no">02</div>
  <h2 class="about-title h-display">About<br>Company</h2>
  <p class="about-col about-col-a body-copy">We are a technical services firm working with clients across engineering, energy and infrastructure. Our teams plan, design and deliver projects of every size, from early studies to full handover. Each project is run by a named lead, with clear reporting and a single point of contact from start to finish, so you always know where the work stands.</p>
  <p class="about-col about-col-b body-copy">Founded by practising engineers, the company has grown steadily through repeat work and referrals. We value plain communication, careful planning, safe sites and honest estimates in every proposal we send.</p>
  <footer class="footer">
    <div class="contact c1"><svg><use href="#i-globe"/></svg>www.corvanetech.com</div>
    <div class="contact c2"><svg><use href="#i-pin"/></svg>48 Harbor Row, Westfield</div>
    <div class="contact c3"><svg><use href="#i-phone"/></svg>+1-555-014-2290</div>
    <div class="contact c4"><svg><use href="#i-mail"/></svg>hello@corvanetech.com</div>
  </footer>
</section>

<!-- Cooperation -->
<section class="page page-coop">
  <div class="photo photo-group" role="img" aria-label="Smiling colleagues gathered around a laptop in an office" style="left:0;top:98px;width:577px;height:304px"></div>
  <svg class="shape" viewBox="0 0 577 815" aria-hidden="true">
    <polygon points="270,22 577,22 577,98 300,98" fill="var(--ink)"/>
    <polygon points="0,18 270,18 300,108 0,108" fill="var(--orange)"/>
    <polygon points="337,0 352,0 402,72 387,72" fill="var(--orange)"/>
  </svg>
  <div class="brand brand-light" style="left:65px;top:52px"><span class="brand-dot"></span>CORVANE</div>
  <div class="page-no">03</div>
  <h2 class="coop-title h-display">Our Most<br>Important<br>Cooperation</h2>
  <p class="coop-copy body-copy" style="top:433px">Our partnerships are built on trust earned over many years of shared projects. We work alongside client teams on site and in the office, combining their knowledge of the operation with our technical expertise, tools and methods.</p>
  <p class="coop-copy body-copy" style="top:490px">Every engagement starts with a short discovery phase to agree goals, risks and success measures. From there we set a realistic plan and keep it updated, so both sides can act quickly when conditions change and decisions are needed.</p>
  <div class="team-point" style="left:58px"><h3>Teamwork 1</h3><p>Joint planning sessions keep scope, budget and timing agreed at every stage.</p></div>
  <div class="team-point" style="left:312px"><h3>Teamwork 2</h3><p>Shared reviews keep quality, safety and progress visible to all parties.</p></div>
  <footer class="footer">
    <div class="contact c1"><svg><use href="#i-globe"/></svg>www.corvanetech.com</div>
    <div class="contact c2"><svg><use href="#i-pin"/></svg>48 Harbor Row, Westfield</div>
    <div class="contact c3"><svg><use href="#i-phone"/></svg>+1-555-014-2290</div>
    <div class="contact c4"><svg><use href="#i-mail"/></svg>hello@corvanetech.com</div>
  </footer>
</section>

<!-- Team -->
<section class="page page-team">
  <svg class="shape" viewBox="0 0 577 815" aria-hidden="true">
    <polygon points="270,22 577,22 577,98 300,98" fill="var(--ink)"/>
    <polygon points="0,18 270,18 300,108 0,108" fill="var(--orange)"/>
    <polygon points="337,0 352,0 402,72 387,72" fill="var(--orange)"/>
  </svg>
  <div class="brand brand-light" style="left:65px;top:52px"><span class="brand-dot"></span>CORVANE</div>
  <div class="page-no">03</div>
  <h2 class="team-title h-display">Meet Our Team</h2>
  <div class="member" style="left:55px;top:208px"><div class="portrait" role="img" aria-label="Portrait photo of Lena Harwood"></div><h4>Lena Harwood</h4><p>Owner</p></div>
  <div class="member" style="left:218px;top:208px"><div class="portrait" role="img" aria-label="Portrait photo of Arif Wibowo"></div><h4>Arif Wibowo</h4><p>Owner</p></div>
  <div class="member" style="left:381px;top:208px"><div class="portrait" role="img" aria-label="Portrait photo of Nora Lee Whitfield"></div><h4>Nora Lee Whitfield</h4><p>Owner</p></div>
  <div class="member" style="left:55px;top:438px"><div class="portrait" role="img" aria-label="Portrait photo of Felix Marlowe"></div><h4>Felix Marlowe</h4><p>Deputy Manager</p></div>
  <div class="member" style="left:218px;top:438px"><div class="portrait" role="img" aria-label="Portrait photo of Daniel Ashcroft"></div><h4>Daniel Ashcroft</h4><p>Manager</p></div>
  <div class="member" style="left:381px;top:438px"><div class="portrait" role="img" aria-label="Portrait photo of Ines Castillo"></div><h4>Ines Castillo</h4><p>Deputy Manager</p></div>
  <footer class="footer">
    <div class="contact c1"><svg><use href="#i-globe"/></svg>www.corvanetech.com</div>
    <div class="contact c2"><svg><use href="#i-pin"/></svg>48 Harbor Row, Westfield</div>
    <div class="contact c3"><svg><use href="#i-phone"/></svg>+1-555-014-2290</div>
    <div class="contact c4"><svg><use href="#i-mail"/></svg>hello@corvanetech.com</div>
  </footer>
</section>

<!-- Closing -->
<section class="page page-end">
  <div class="brand" style="left:42px;top:72px"><span class="brand-dot"></span>CORVANE</div>
  <svg class="shape" viewBox="0 0 577 815" aria-hidden="true">
    <polygon points="0,108 125,108 265,478 0,478" fill="var(--orange)"/>
    <polygon points="388,122 440,35 470,122" fill="var(--orange-dark)"/>
    <polygon points="440,35 505,35 577,160 577,240" fill="var(--orange)"/>
    <polygon points="245,442 285,442 265,478" fill="var(--orange-dark)"/>
  </svg>
  <div class="photo photo-building" role="img" aria-label="Upward view of a glass office tower framed by tree branches" style="left:0;top:122px;width:577px;height:320px;clip-path:polygon(125px 0,577px 0,577px 320px,245px 320px)"></div>
  <div class="end-kicker">End Of Proposal</div>
  <h2 class="end-title h-display">THANK<br>YOU</h2>
  <div class="rule" style="left:58px;top:634px;height:3px;width:57px"></div>
  <p class="end-lead">Thank you for considering our proposal. We look forward to working with your team and are glad to answer any questions about the scope, schedule or pricing.</p>
  <footer class="footer">
    <div class="contact c1"><svg><use href="#i-globe"/></svg>www.corvanetech.com</div>
    <div class="contact c2"><svg><use href="#i-pin"/></svg>48 Harbor Row, Westfield</div>
    <div class="contact c3"><svg><use href="#i-phone"/></svg>+1-555-014-2290</div>
    <div class="contact c4"><svg><use href="#i-mail"/></svg>hello@corvanetech.com</div>
  </footer>
</section>
</body>
</html>
```